Business Card Design Project

I own a dental practice and would like to use a logo that was recently designed to make business cards.
I am looking for a clean card with the following information on the card.

Halvorsen Dental Center (Using the logo)
Martin L. Halvorsen, D.D.S.
7234 Pinewick Ave. Suite B
Colorado Springs, CO 80547
(719) 482-6130
halvorsendentalcenter@mailbox-example.net
www.halvorsendentalcenter.example

Also a list of items on the back:
Services include

Family Dentistry
Cosmetic
Whitening
Tooth Colored Fillings
Crowns/Bridges
Implants/Tooth Replacement
Dentures
Root Canals
Updates

Just an FYI, I added an email address and website address.

I also added my Pic.  Please give designs with and without the pic

Thanks

Target Market(s)

20-70 U.S. Female that handles the household budget.

Industry/Entity Type

Dental

Requirements
Must have
• The logo is key. The color scheme of the logo is also key. The back of the business card should have the list of Dental Services offered at the practice. The front should be clean and professional looking. No cartoons. I will also include a picture of myself. I think that the final card may or may not include this picture, so the card designs should come with and without the picture. USE THE BLUE LOGO ONLY!!!
Should not have
• NO teeth should be on the card.

```html
<!DOCTYPE html>
<html lang="en">
<head>
<meta charset="utf-8">
<title>Halvorsen Dental Center – Business Cards</title>
<link rel="stylesheet" href="https://fonts.googleapis.com/css2?family=Open+Sans:wght@300;400;600;700&display=swap">
<style>
  :root {
    --page-bg: #e9e6e1;
    --card-white: #ffffff;
    --brand-teal: #2c6b87;
    --brand-teal-dark: #24596f;
    --swoosh-deep: #3d6d84;
    --swoosh-soft: #a7bfcb;
    --name-blue: #4f8ba6;
    --ink: #4a4444;
    --ink-soft: #6b6566;
    --leaf-pale: #c9d6de;
    --white: #ffffff;
  }
  * { box-sizing: border-box; margin: 0; padding: 0; }
  html, body {
    width: 1200px; height: 1024px; overflow: hidden;
    background: var(--page-bg);
    font-family: "Open Sans", Arial, sans-serif;
  }
  .card {
    position: absolute; left: 200px;
    width: 800px; height: 457px;
    border-radius: 4px; overflow: hidden;
    box-shadow: 0 6px 18px rgba(0,0,0,0.18);
  }
  /* ---------- front ---------- */
  .card-front { top: 40px; background: var(--card-white); }
  .front-swoosh { position: absolute; inset: 0; }
  .brand-block {
    position: absolute; left: 60px; top: 92px;
    display: flex; align-items: center; gap: 20px;
  }
  .brand-dot {
    width: 54px; height: 54px; border-radius: 50%;
    background: var(--brand-teal);
  }
  .brand-name {
    color: var(--ink); font-weight: 400;
    font-size: 34px; line-height: 1.08; letter-spacing: 0.5px;
  }
  .brand-tagline {
    margin-top: 6px; font-size: 13px; letter-spacing: 1.6px;
    color: var(--ink-soft); font-weight: 400;
  }
  .divider {
    position: absolute; left: 410px; top: 70px;
    width: 2px; height: 120px; background: #b9c4ca;
  }
  .contact-list {
    position: absolute; left: 430px; top: 82px;
    list-style: none; font-size: 14px; color: var(--ink);
    white-space: nowrap;
  }
  .contact-list li { display: flex; align-items: center; gap: 9px; margin-bottom: 10px; }
  .contact-list svg { width: 14px; height: 14px; flex: none; }
  .person {
    position: absolute; left: 60px; top: 262px; color: var(--ink);
  }
  .person-name {
    font-size: 19px; font-weight: 700; letter-spacing: 1px;
    color: var(--name-blue);
  }
  .person-name .credential { color: var(--ink-soft); font-weight: 600; font-size: 15px; }
  .person-address { margin-top: 10px; font-size: 17px; line-height: 1.45; }
  /* ---------- back ---------- */
  .card-back {
    top: 537px;
    background: linear-gradient(160deg, #34799a 0%, var(--brand-teal) 55%, var(--brand-teal-dark) 100%);
    color: var(--white);
  }
  .branch-art {
    position: absolute; left: 20px; top: 0; width: 520px; height: 270px;
    background: radial-gradient(ellipse closest-side at 50% 50%, rgba(201,214,222,0.42) 0%, rgba(201,214,222,0.18) 50%, rgba(201,214,222,0) 100%);
  }
  .back-brand {
    position: absolute; left: 420px; top: 168px;
    font-size: 30px; font-weight: 400; line-height: 1.08; letter-spacing: 0.5px;
  }
  .back-tagline {
    position: absolute; left: 420px; top: 240px;
    font-size: 13px; letter-spacing: 1.6px;
  }
  .services {
    position: absolute; left: 60px; top: 292px;
    list-style: none; font-size: 15px; line-height: 1.7; font-weight: 300;
  }
  .services li { display: flex; align-items: center; gap: 8px; }
  .bullet { width: 7px; height: 7px; border-radius: 50%; background: var(--leaf-pale); }
  .back-web {
    position: absolute; left: 60px; top: 395px;
    font-size: 15px; font-weight: 300;
  }
</style>
</head>
<body>

<section class="card card-front">
  <svg class="front-swoosh" viewBox="0 0 800 457" preserveAspectRatio="none" aria-hidden="true">
    <path d="M0 457 L0 440 C260 430 520 360 800 210 L800 457 Z" fill="var(--swoosh-soft)"/>
    <path d="M0 457 C300 445 560 380 800 250 L800 457 Z" fill="var(--swoosh-deep)"/>
    <path d="M120 457 C380 440 600 370 800 268" stroke="#ffffff" stroke-width="3" fill="none" opacity="0.85"/>
  </svg>

  <div class="brand-block">
    <span class="brand-dot"></span>
    <div>
      <div class="brand-name">Halvorsen<br>Dental Center</div>
      <div class="brand-tagline">FAMILY · COSMETIC · IMPLANTS</div>
    </div>
  </div>

  <div class="divider"></div>

  <ul class="contact-list">
    <li>
      <svg viewBox="0 0 16 16"><path d="M4 1 L6.5 4 L5 6 C6 8 8 10 10 11 L12 9.5 L15 12 L13 15 C7 14 2 9 1 3 Z" fill="var(--ink)"/></svg>
      (719) 482-6130
    </li>
    <li>
      <svg viewBox="0 0 16 16"><rect x="1" y="3" width="14" height="10" fill="var(--ink)"/><path d="M1 3 L8 9 L15 3" stroke="#fff" stroke-width="1.3" fill="none"/></svg>
      halvorsendentalcenter@mailbox-example.net
    </li>
    <li>
      <svg viewBox="0 0 16 16"><circle cx="8" cy="8" r="7" fill="var(--ink)"/><path d="M1 8 H15 M8 1 C4 5 4 11 8 15 M8 1 C12 5 12 11 8 15" stroke="#fff" stroke-width="1" fill="none"/></svg>
      www.halvorsendentalcenter.example
    </li>
  </ul>

  <div class="person">
    <div class="person-name">MARTIN L. HALVORSEN <span class="credential">| D.D.S.</span></div>
    <div class="person-address">7234 Pinewick Ave. Suite B<br>Colorado Springs, CO 80547</div>
  </div>
</section>

<section class="card card-back">
  <div class="branch-art" role="img" aria-label="Decorative branch with pale leaves"></div>
  <div class="back-brand">Halvorsen<br>Dental Center</div>
  <div class="back-tagline">FAMILY · COSMETIC · IMPLANTS</div>
  <ul class="services">
    <li>Family Dentistry <span class="bullet"></span> Cosmetic <span class="bullet"></span> Whitening</li>
    <li>Tooth Colored Fillings <span class="bullet"></span> Crowns/Bridges</li>
    <li>Implants/Tooth Replacement <span class="bullet"></span> Dentures <span class="bullet"></span> Root Canals</li>
  </ul>
  <div class="back-web">www.halvorsendentalcenter.example</div>
</section>

</body>
</html>
```